Startup photography business has a new logo, now we need business cards

Design a business card for the two partners of our business.
Our business Brisk Wombat has a new logo and we need to design a business card to showcase it and us.
Our colours of blue and orange are punchy and vivid, but how can we make the most of it on our card?

It should have our name Brisk Wombat
name of partner
phone number
email
website

Industry/Entity Type

Professional Photography

Contact Information for Business Card

Ewan Pottsworth
+61 455 81 76 93
ewan@briskwombat.com.au
briskwombat.com.au

second card
Liam Fairley
+61 419 628 315
liam@briskwombat.com.au
briskwombat.com.au

Colors
f37122
f68d4c
33a6d7
0592cd

Requirements
Must have
• one version of our logo, we have included options
• Name
• phone number
• email
• website
Nice to have
• instagram briskwombatstudio
• twitter briskwombatstudio
• facebook briskwombatstudio

```html
<!DOCTYPE html>
<html lang="en">
<head>
<meta charset="utf-8">
<title>Brisk Wombat — Business Card</title>
<link rel="stylesheet" href="https://fonts.googleapis.com/css2?family=Open+Sans:wght@400;600;700&display=swap">
<style>
  :root {
    --backdrop: #2e2e2e;
    --brand-blue: #29a3d9;
    --ink: #1a1a1a;
    --paper: #ffffff;
    --rule: #222222;
  }
  * { box-sizing: border-box; margin: 0; padding: 0; }
  html, body {
    width: 1200px; height: 900px; overflow: hidden;
    background: var(--backdrop);
    font-family: "Open Sans", Arial, sans-serif;
  }
  .stage {
    position: relative; width: 1200px; height: 900px;
  }
  .card {
    position: absolute; left: 260px;
    width: 680px; height: 390px;
    border-radius: 26px;
    overflow: hidden;
    box-shadow: 0 18px 40px rgba(0,0,0,.45);
  }
  .card--front { top: 40px; background: var(--brand-blue); }
  .card--back { top: 470px; background: var(--paper); }

  /* front */
  .front-mark {
    position: absolute; left: 0; right: 0; top: 130px;
    display: flex; align-items: center; justify-content: center; gap: 16px;
  }
  .front-mark__dot {
    width: 64px; height: 64px; border-radius: 50%; background: var(--paper);
  }
  .front-mark__name {
    color: var(--paper); font-weight: 700; font-size: 46px; letter-spacing: 1px;
    text-transform: uppercase;
  }
  .social-dots {
    position: absolute; left: 0; right: 0; top: 300px;
    display: flex; justify-content: center; gap: 12px;
  }
  .social-dots span {
    width: 14px; height: 14px; border-radius: 50%; background: var(--paper);
  }

  /* back */
  .back-mark {
    position: absolute; left: 44px; top: 96px;
    display: flex; flex-direction: column; align-items: flex-start; gap: 10px;
  }
  .back-mark__dot {
    width: 70px; height: 70px; border-radius: 50%; background: var(--brand-blue);
    margin-left: 40px;
  }
  .back-mark__name {
    color: var(--brand-blue); font-weight: 700; font-size: 28px;
    text-transform: uppercase; letter-spacing: 1px; white-space: nowrap;
  }
  .contact {
    position: absolute; right: 40px; top: 112px;
    text-align: right;
  }
  .contact__name {
    font-weight: 700; font-size: 23px; text-transform: uppercase;
    padding-bottom: 5px; border-bottom: 2px solid var(--rule);
    margin-bottom: 8px; color: var(--ink); white-space: nowrap;
  }
  .contact__first { color: var(--brand-blue); font-weight: 600; }
  .contact__line {
    display: flex; justify-content: flex-end; align-items: center; gap: 8px;
    font-size: 14px; color: var(--ink); line-height: 21px; white-space: nowrap;
  }
  .contact__line svg { width: 13px; height: 13px; flex: none; }
  .base-rule {
    position: absolute; left: 0; right: 0; top: 318px;
    border-top: 2px solid var(--rule);
  }
</style>
</head>
<body>
<main class="stage">
  <section class="card card--front" aria-label="Card front">
    <div class="front-mark">
      <span class="front-mark__dot"></span>
      <span class="front-mark__name">Brisk Wombat</span>
    </div>
    <div class="social-dots" aria-label="Social channels: briskwombatstudio">
      <span></span><span></span><span></span>
    </div>
  </section>

  <section class="card card--back" aria-label="Card back">
    <div class="back-mark">
      <span class="back-mark__dot"></span>
      <span class="back-mark__name">Brisk Wombat</span>
    </div>
    <div class="contact">
      <h1 class="contact__name"><span class="contact__first">Ewan</span> Pottsworth</h1>
      <p class="contact__line">+61 455 81 76 93
        <svg viewBox="0 0 16 16"><path d="M4 1l3 3-2 2c1 2 3 4 5 5l2-2 3 3-2 3C7 15 1 9 1 3z" fill="none" stroke="#29a3d9" stroke-width="1.5"/></svg>
      </p>
      <p class="contact__line">ewan@briskwombat.com.au
        <svg viewBox="0 0 16 16"><rect x="1" y="3" width="14" height="10" fill="none" stroke="#29a3d9" stroke-width="1.5"/><path d="M1 3l7 6 7-6" fill="none" stroke="#29a3d9" stroke-width="1.5"/></svg>
      </p>
      <p class="contact__line">www.briskwombat.com.au
        <svg viewBox="0 0 16 16"><circle cx="8" cy="8" r="6.5" fill="none" stroke="#29a3d9" stroke-width="1.5"/><path d="M1.5 8h13M8 1.5c-3 3-3 10 0 13M8 1.5c3 3 3 10 0 13" fill="none" stroke="#29a3d9" stroke-width="1.2"/></svg>
      </p>
    </div>
    <div class="base-rule"></div>
  </section>
</main>
</body>
</html>
```